Managed IT services business card design

We haven't needed a business card since the founding of the business in 2005. All our clients have been coming through word of mouth. And lately more and more existing clients are requesting for our business cards to pass on to their contacts in recommending us.
So we needing a business card design. We use various innovative solutions and methodologies to provide IT services to small businesses in managing their IT systems. Our role is the same as an in-house, full-time IT Manager for our clients, but outsourced. So we take care of all our clients' IT needs, just as an IT Manager would be expected to perform.
We have a holding website, which we're happy to leave for now. If we can use the same logo would be great - www.tegvu.com.au
Preferred colours are shades of are white, grey and black.
We pride our business with the following traits: proactive, good service, prompt response, trustworthy.
Target Market(s)
Small businesses of any industry
Industry/Entity Type
Business

```html
<!DOCTYPE html>
<html lang="en">
<head>
<meta charset="utf-8">
<title>tegvu business card</title>
<link href="https://fonts.googleapis.com/css2?family=Open+Sans:wght@400&display=swap" rel="stylesheet">
<style>
  :root {
    --backdrop: #c4c4c4;
    --card: #ffffff;
    --ink: #1e1e1e;
    --ink-soft: #3a3a3a;
    --rule: #2a2a2a;
    --icon: #555555;
  }
  * { box-sizing: border-box; margin: 0; padding: 0; }
  html, body {
    width: 1200px;
    height: 900px;
    overflow: hidden;
    background: var(--backdrop);
    font-family: "Open Sans", sans-serif;
    color: var(--ink);
  }
  .stage {
    position: relative;
    width: 1200px;
    height: 900px;
  }
  .card {
    position: absolute;
    top: 300px;
    width: 520px;
    height: 300px;
    background: var(--card);
    border-radius: 26px;
    box-shadow: 0 14px 30px rgba(0,0,0,0.18);
  }
  .card--front { left: 50px; }
  .card--back { left: 630px; }

  .brand-name {
    position: absolute;
    top: 82px;
    left: 0;
    width: 100%;
    text-align: center;
    font-weight: 400;
    font-size: 30px;
    line-height: 1.2;
    letter-spacing: 0;
    color: var(--ink);
  }
  .card__rule {
    position: absolute;
    top: 152px;
    left: 0;
    width: 100%;
    height: 2px;
    background: var(--rule);
  }
  .person {
    position: absolute;
    top: 188px;
    left: 0;
    width: 196px;
    text-align: right;
  }
  .person__name {
    font-size: 19px;
    font-weight: 400;
    line-height: 1.2;
  }
  .person__title {
    font-size: 11px;
    color: var(--ink-soft);
  }
  .card__divider {
    position: absolute;
    top: 180px;
    left: 212px;
    width: 1.5px;
    height: 96px;
    background: var(--rule);
  }
  .contact {
    position: absolute;
    top: 184px;
    left: 226px;
    list-style: none;
    font-size: 15px;
    line-height: 20px;
    color: var(--ink);
  }
  .contact__item {
    display: flex;
    align-items: flex-start;
    gap: 6px;
  }
  .contact__icon {
    width: 14px;
    height: 14px;
    margin-top: 3px;
    flex: none;
    fill: var(--icon);
  }
  .support {
    position: absolute;
    top: 140px;
    left: 0;
    width: 100%;
    text-align: center;
    font-size: 15px;
    color: var(--ink);
  }
</style>
</head>
<body>
<main class="stage">
  <section class="card card--front" aria-label="Card front">
    <p class="brand-name">tegvu</p>
    <div class="card__rule"></div>
    <div class="person">
      <p class="person__name">Liam Torres</p>
      <p class="person__title">Director</p>
    </div>
    <div class="card__divider"></div>
    <ul class="contact">
      <li class="contact__item">
        <svg class="contact__icon" viewBox="0 0 14 14" aria-hidden="true"><path d="M4 0h6a1 1 0 0 1 1 1v12a1 1 0 0 1-1 1H4a1 1 0 0 1-1-1V1a1 1 0 0 1 1-1zm0.5 1.5v9h5v-9zM7 11.5a0.8 0.8 0 1 0 0 1.6a0.8 0.8 0 1 0 0-1.6z"/></svg>
        <span>0412 555 018</span>
      </li>
      <li class="contact__item">
        <svg class="contact__icon" viewBox="0 0 14 14" aria-hidden="true"><path d="M1 3c0-1.5 2.5-2.5 6-2.5s6 1 6 2.5v1.5h-3V3H4v1.5H1zM3.5 6h7l2 7h-11zM7 7.6a1.8 1.8 0 1 0 0 3.6a1.8 1.8 0 1 0 0-3.6z"/></svg>
        <span>03 9555 0142</span>
      </li>
      <li class="contact__item">
        <svg class="contact__icon" viewBox="0 0 14 14" aria-hidden="true"><path d="M0.5 3h13v9h-13zM1.8 4.2v0.3L7 8l5.2-3.5v-0.3zM1.8 6v4.8h10.4V6L7 9.5z"/></svg>
        <span>liam.torres@tegvu.com.au</span>
      </li>
      <li class="contact__item">
        <svg class="contact__icon" viewBox="0 0 14 14" aria-hidden="true"><path d="M7 1l6.5 6h-2v6H8.5V9.5h-3V13h-3V7h-2z"/></svg>
        <span>Level 4, 87 Carrow Street,<br>Melbourne VIC 3000</span>
      </li>
    </ul>
  </section>

  <section class="card card--back" aria-label="Card back">
    <p class="support">support@tegvu.com.au</p>
  </section>
</main>
</body>
</html>
```